New Artwork/Design for Established Weight Loss Podcast

Hello,
I would like new artwork/design for my podcast. It's called Bright Path Slimdown and has been a consistently top 50 show in the fitness/nutrition category on Orbix. My current design was originally created when I started the podcast over 2 years ago. It's time to refresh and update things! I would like a new design that incorporates a photo of me, but could also be used as a standalone logo for the podcast without my photo. A nice, clean, professional, yet fun design. Here is a Vantor drive link with professional photos that could be used:
https://files.example-share.net/folders/7Qkrt58x-p2mLWHtabvPXsaQ9Ro6JwZ3k?usp=sharing

Here's a little more about the show . There are three big taglines. These do NOT need to be included on the design. I just include them here to help with the feel/theme of the design.

1: To change your body, you must first change your brain.
2: There's so much more to you than just a number (what you weigh).
3: Losing weight is really about gaining life and living the life you've always wanted.

This podcast is all about busy moms, dads, husbands, wives who are working, raising kids, and trying to juggle everything life’s throwing at them … but also want to be the best they can for their family and friends and loved ones.

The podcast is NOT about how to get six-pack abs or how to drop as much weight as possible in 8 weeks. It's about finding sustainable success with your body, peace of mind with food, and improving your relationship with yourself.

Week by week, I provide bite-sized guidance - 20-25 minute episodes that pull back the curtain and reveal the truth about what it takes to lose weight and gain life - what strategy and approach real people are using to get results while escaping the soul-sucking, all-or-nothing diet mentality.

Here's a link to the current artwork: https://files.example-share.net/file/d/4T2bHn8qsvkeTrmzYpRd-ab3KNJ-m-QXZ/view?usp=sharing

And the logo without my photo: https://files.example-share.net/file/d/8JN5pKa3Rw_h2b74cFxYqPmE6zGtdLs/view?usp=sharing

I'm open to any colors, but something that either matches the colors of my website or signature "Move Glow Trim Down" program would probably be a smart idea. Here are links to my website and the MGTD logo . . .

Website: https://danemarshwellness.example/

MGTD logo:
https://files.example-share.net/file/d/5VQpLm2Kxe_Tw9Hr4zNgUa7YcBfsjdP/view?usp=sharing

Happy to answer any questions you might have. Thanks.

Target Market(s)

35 to 55 years old, roughly 70% female, 30% male, professionals, primarily in the U.S. and Canada

Industry/Entity Type

nutrition, health, weight loss

Requirements
Must have
• One version with my photo and the same design without my photo
Nice to have
• Open to any colors, but possibly incorporate colors from either my website or MGTD logo (see project description for more info)
Should not have
• Any hardcore fitness or bodybuilding imagery

```html
<!DOCTYPE html>
<html lang="en">
<head>
<meta charset="utf-8">
<title>Bright Path Slimdown – Podcast Artwork</title>
<link href="https://fonts.googleapis.com/css2?family=Barlow+Condensed:wght@500&family=Montserrat:wght@600&family=Poppins:wght@400;600&display=swap" rel="stylesheet">
<style>
  :root {
    --page: #ffffff;
    --sky: #e2f4f6;
    --teal: #72c7d0;
    --teal-soft: #a9d5da;
    --sun: #fdc24a;
    --navy: #14384f;
    --photo-dark: #2a2d31;
    --photo-mid: #6a5a50;
    --play: #5cc5cd;
    --ink: #555a5e;
    --ink-soft: #6b6f73;
    --rule: #e3e3e3;
    --track: #cfcfcf;
  }
  * { box-sizing: border-box; margin: 0; padding: 0; }
  html, body { width: 1200px; height: 1200px; overflow: hidden; background: var(--page); }
  .sheet { position: relative; width: 1200px; height: 1200px; }

  .cover {
    position: absolute; left: 281px; top: 95px; width: 638px; height: 638px;
    box-shadow: 0 14px 34px rgba(0,0,0,.22);
  }
  .cover svg, .player__art svg { display: block; width: 100%; height: 100%; }

  .wordmark { font-family: "Barlow Condensed", sans-serif; font-weight: 500; fill: var(--navy); }
  .byline { font-family: "Montserrat", sans-serif; font-weight: 600; fill: var(--navy); letter-spacing: 7px; }

  .player {
    position: absolute; left: 204px; top: 828px; width: 786px; height: 230px;
    border: 1px solid var(--rule); border-radius: 4px; background: #fff;
    font-family: "Poppins", sans-serif;
    box-shadow: 0 1px 3px rgba(0,0,0,.05);
  }
  .player__art { position: absolute; left: 19px; top: 16px; width: 193px; height: 193px; }
  .player__title {
    position: absolute; left: 229px; top: 36px; width: 380px;
    font-size: 20px; line-height: 29px; font-weight: 600; color: var(--ink);
  }
  .player__meta { position: absolute; left: 229px; top: 96px; font-size: 13px; color: var(--ink-soft); }
  .player__brand {
    position: absolute; right: 22px; top: 20px; display: flex; align-items: center; gap: 5px;
    font-size: 11px; font-weight: 600; color: #222;
  }
  .player__brand i { width: 14px; height: 14px; border-radius: 50%; background: #222; display: block; }
  .player__play {
    position: absolute; left: 229px; top: 156px; width: 48px; height: 48px; border-radius: 50%;
    background: var(--play);
  }
  .player__play::after {
    content: ""; position: absolute; left: 19px; top: 15px;
    border-left: 14px solid #fff; border-top: 9px solid transparent; border-bottom: 9px solid transparent;
  }
  .player__time { position: absolute; top: 152px; font-size: 12px; color: var(--ink-soft); }
  .player__time--start { left: 297px; }
  .player__time--end { right: 22px; }
  .player__track { position: absolute; left: 297px; right: 22px; top: 172px; height: 4px; border-radius: 2px; background: var(--track); }
  .player__controls {
    position: absolute; left: 305px; top: 186px; display: flex; align-items: center; gap: 18px;
    color: var(--ink-soft); font-size: 15px;
  }
  .player__controls svg { width: 18px; height: 18px; }
  .player__links {
    position: absolute; right: 26px; top: 189px; display: flex; gap: 19px; align-items: center;
    font-size: 12px; color: var(--ink-soft); letter-spacing: .3px;
  }
  .player__dots { font-size: 14px; letter-spacing: 2px; color: #555; font-weight: 600; }
</style>
</head>
<body>
<svg width="0" height="0" style="position:absolute" aria-hidden="true">
  <defs>
    <linearGradient id="photo-tone" x1="0" y1="0" x2="0" y2="1">
      <stop offset="0" stop-color="#8a6f60"/>
      <stop offset=".3" stop-color="var(--photo-dark)"/>
      <stop offset="1" stop-color="#2f3d52"/>
    </linearGradient>
    <symbol id="cover-art" viewBox="0 0 638 638">
      <rect class="cover__sky" width="638" height="638" fill="#e2f4f6"/>
      <polygon class="cover__sun-top" points="347,0 638,0 638,275 460,150" fill="#fdc24a"/>
      <polygon class="cover__stripe-top" points="318,0 347,0 470,160 445,175" fill="#72c7d0"/>
      <polygon class="cover__band" points="119,547 638,470 638,638 190,638" fill="#a9d5da"/>
      <polygon class="cover__sun-bottom" points="0,418 0,638 160,638" fill="#fdc24a"/>
      <polygon class="cover__stripe-bottom" points="0,400 0,418 160,638 190,638" fill="#72c7d0"/>
      <path class="cover__photo" role="img" aria-label="Portrait photo of the host, smiling, seated in a dark hoodie and jeans"
            d="M440,120 Q470,100 505,115 Q535,140 530,190 L560,240 Q620,270 638,290 L638,638 L345,638 Q390,600 420,560 L440,280 Q450,250 470,240 Q440,200 440,120 Z"
            fill="url(#photo-tone)"/>
      <text class="wordmark" x="56" y="213" font-size="74">BRIGHT PATH</text>
      <text class="wordmark" x="56" y="281" font-size="74">SLIMDOWN</text>
      <rect x="56" y="296" width="370" height="4" fill="#14384f"/>
      <text class="byline" x="50" y="330" font-size="19">WITH DANE MARSH</text>
      <text class="byline" x="290" y="358" font-size="15">PODCAST</text>
    </symbol>
  </defs>
</svg>

<main class="sheet">
  <div class="cover">
    <svg viewBox="0 0 638 638" role="img" aria-label="Bright Path Slimdown podcast cover"><use href="#cover-art"/></svg>
  </div>

  <section class="player">
    <div class="player__art">
      <svg viewBox="0 0 638 638" role="img" aria-label="Podcast cover thumbnail"><use href="#cover-art"/></svg>
    </div>
    <div class="player__brand"><i></i>Castwell</div>
    <h2 class="player__title">Four of The Biggest Weight Loss Misconceptions</h2>
    <p class="player__meta">Episode 228 • 14th February 2023 • Bright Path Slimdown • Dane Marsh</p>
    <div class="player__play" aria-label="Play"></div>
    <span class="player__time player__time--start">00:00:00</span>
    <span class="player__time player__time--end">00:22:20</span>
    <div class="player__track"></div>
    <div class="player__controls">
      <svg viewBox="0 0 20 20" fill="none" stroke="#666" stroke-width="1.6"><path d="M6 5 A7 7 0 1 1 4 11"/><path d="M6 1 L6 5 L10 5"/></svg>
      <svg viewBox="0 0 20 20" fill="none" stroke="#666" stroke-width="1.6"><path d="M14 5 A7 7 0 1 0 16 11"/><path d="M14 1 L14 5 L10 5"/></svg>
      <span>1×</span>
      <svg viewBox="0 0 20 20" fill="#666"><path d="M3 7 H7 L11 3 V17 L7 13 H3 Z"/><path d="M14 6 Q17 10 14 14" stroke="#666" stroke-width="1.6" fill="none"/></svg>
    </div>
    <nav class="player__links">
      <span>NOTES</span><span>LINKS</span><span>FOLLOW</span><span class="player__dots">•••</span>
    </nav>
  </section>
</main>
</body>
</html>
```